Business Identity Stationary

Already have the logo which is in the attached files so only need the Business STationary
1) Double Sided Business Card
2) Letterhead
3) Presentation folder with business card holder on inside cover
4) WIth compliments slip
See information for business cards, letterhead and presentation folder below.
http://files.pixelbazaar-example.com/img/771204/40612/40612_3918825_771204_thumb.jpg
Updates

This should be a simply job using a logo we already had designed along with a little device. I suggest using the device off center and perhaps lower in the corner in an abstract way. Also the logo device could be used as a watermark for the letterhead. The designer who created the logo presented something that I think works well for a business card. The front of the double sided business card could have the name logo small for the website address and only use the Lime device on the front. Then on the back could be the name Brevar Consulting logo.

Please note that for the business card the black and lime green background do look good. Also please think of using the lime device separately in an unusual way.

It has been brought to my attention that.my budget was far to low. Hopefully this.will attract you to the project. 

The parent company of Brevar Consulting is TallHeron investments. I have uploaded a file of the Tall Heron business card I really like. Perhaps use this business card as a guide to the type of modern and clean style I am looking for. It also works to have the Brevar Consultign and Tall Heron similar.

Reason: Still haven't received anything exactly right.

Industry/Entity Type

Business

Font styles to use
Sans Serif

Colors
9bcb3c
000000
5c5c5c
add136
cadf82
eaf2cf
f9fbf2
1b1b1b
757575

Requirements
Must have
• 1) Double Sided Business Card
Marta Delvorin
Director
Tel: +505 8290 3357
Email: mkd@brevarconsulting-example.com
Website: www.brevarconsulting-example.com

Everett Delvorin
Director
Tel: +505 8290 3362
Email: ekd@brevarconsulting-example.com

Lucia Pardo Ventrosa
Director
Tel: 8442 6183
Email: lpv@brevarconsulting-example.com

2) Letterhead
Logo
Lime Logo Device
Website Address: www.brevarconsulting-example.com
Small print on bottom: Brevar Consulting a Tall Heron Investment Company SA. RUC K0720000483915

3) Presentation Folder
Traditional Presentation folder with inside front cover spot for the insertion of business card.

4) With Compliments slip

```html
<!DOCTYPE html>
<html lang="en">
<head>
<meta charset="utf-8">
<title>Brevar Consulting — Business Card</title>
<link rel="stylesheet" href="https://fonts.googleapis.com/css2?family=Lato:wght@400;700&display=swap">
<style>
  :root {
    --backdrop: #2a2a2a;
    --card-white: #f9f9f8;
    --card-green: #5e7a33;
    --lime: #9bcb3c;
    --lime-soft: #add136;
    --ink: #1b1b1b;
    --ink-mid: #333333;
    --white: #f4f4f0;
  }
  * { margin: 0; padding: 0; box-sizing: border-box; }
  html, body { width: 1200px; height: 900px; overflow: hidden; }
  body {
    background: var(--backdrop);
    font-family: "Lato", Arial, sans-serif;
    position: relative;
  }
  .card {
    position: absolute;
    left: 355px;
    width: 486px;
    height: 270px;
    box-shadow: 0 2px 6px rgba(0,0,0,0.45);
  }
  .card--front { top: 158px; background: var(--card-white); }
  .card--back { top: 467px; background: var(--card-green); }

  .wordmark { position: absolute; display: flex; align-items: center; gap: 12px; }
  .wordmark__dot { width: 26px; height: 26px; border-radius: 50%; background: var(--lime); flex: none; }
  .wordmark__text { font-weight: 400; line-height: 1; }
  .wordmark__name { display: block; font-size: 54px; letter-spacing: 1px; }
  .wordmark__sub { display: block; font-size: 23px; letter-spacing: 7px; margin-top: 6px; }

  .card--front .wordmark { left: 30px; top: 34px; }
  .card--front .wordmark__text { color: var(--ink); }

  .card--back .wordmark { left: 50%; top: 50%; transform: translate(-50%, -50%); }
  .card--back .wordmark__text { color: var(--white); }

  .rule {
    position: absolute; left: 15px; top: 175px;
    width: 262px; height: 1px; background: var(--lime-soft);
  }
  .person { position: absolute; left: 288px; top: 145px; color: var(--ink); }
  .person__name { font-size: 19px; font-weight: 400; letter-spacing: 0.5px; text-transform: uppercase; }
  .person__role { font-size: 12px; margin-top: 4px; }

  .contacts { position: absolute; left: 273px; top: 214px; list-style: none; font-size: 11.5px; color: var(--ink-mid); }
  .contacts li { display: flex; align-items: center; gap: 8px; height: 17px; }
  .contacts svg { width: 9px; height: 10px; fill: var(--lime); flex: none; }

  .website { position: absolute; left: 30px; top: 232px; font-size: 12px; color: var(--ink-mid); }
  .website__domain { color: var(--lime); }
</style>
</head>
<body>
  <section class="card card--front" aria-label="Business card front">
    <div class="wordmark">
      <div class="wordmark__text">
        <span class="wordmark__name">BREVAR</span>
        <span class="wordmark__sub">consulting</span>
      </div>
      <span class="wordmark__dot"></span>
    </div>
    <div class="rule"></div>
    <div class="person">
      <p class="person__name">Marta Delvorin</p>
      <p class="person__role">Director</p>
    </div>
    <ul class="contacts">
      <li>
        <svg viewBox="0 0 9 10" aria-hidden="true"><path d="M2 0h5a1 1 0 0 1 1 1v8a1 1 0 0 1-1 1H2a1 1 0 0 1-1-1V1a1 1 0 0 1 1-1zm.5 1.2v6h4v-6zM4 8a.6.6 0 1 0 1 0 .6.6 0 1 0-1 0z"/></svg>
        <span>+505 8290 3357</span>
      </li>
      <li>
        <svg viewBox="0 0 9 10" aria-hidden="true"><path d="M0 2.5h9v1L4.5 6 0 3.5zM0 4.6l4.5 2.5L9 4.6V8H0z"/></svg>
        <span>mkd@brevarconsulting-example.com</span>
      </li>
    </ul>
    <p class="website">www.<span class="website__domain">brevarconsulting-example</span>.com</p>
  </section>

  <section class="card card--back" aria-label="Business card back">
    <div class="wordmark">
      <div class="wordmark__text">
        <span class="wordmark__name">BREVAR</span>
        <span class="wordmark__sub">consulting</span>
      </div>
      <span class="wordmark__dot"></span>
    </div>
  </section>
</body>
</html>
```